Lakeshore Freightways Council Web Update

Update wordpress based association web site. Please look up www.lakeshorefreightwayscouncil.com for our web site to get a feel for what we currently having. We would like our updated web site to look similar to: www.brightoakfund.com. We will provide our key points for updating in a future email.

Target Market(s)

duplicate the brightoakfund.com format please.

Number of Pages Required

4 page

Font styles to use
Serif

Requirements
Must have
• duplicate the brightoakfund.com format please. You will keep most of the content that we currently have on our website.
Nice to have
• n/a
Should not have
• n/a

```html
<!DOCTYPE html>
<html lang="en">
<head>
<meta charset="utf-8">
<title>Lakeshore Freightways Council</title>
<link rel="stylesheet" href="https://fonts.googleapis.com/css2?family=Libre+Baskerville:wght@400;700&family=EB+Garamond:wght@400;600&family=Old+Standard+TT:wght@400&family=Montserrat:wght@500;600&display=swap">
<style>
:root{
  --navy:#0c0a70;
  --navy-deep:#07064f;
  --panel:rgba(28,24,140,.62);
  --white:#ffffff;
  --topbar:#e9e9ec;
  --ink:#222;
  --grey:#8b8b8b;
}
*{box-sizing:border-box;margin:0;padding:0}
html,body{width:1200px;height:3550px;overflow:hidden;background:#fff}
body{position:relative;font-family:"EB Garamond",Georgia,serif;color:var(--ink)}
.abs{position:absolute}
.topbar{left:0;top:0;width:1200px;height:24px;background:var(--topbar)}
.header{left:0;top:24px;width:1200px;height:94px;background:#fff}
.brand{left:48px;top:14px;color:var(--navy);font-family:"Old Standard TT",Georgia,serif;line-height:1}
.brand-mark{font-size:38px;letter-spacing:1px}
.brand-name{font-size:10.5px;margin-top:4px;width:95px;line-height:1.15;text-transform:uppercase;border-top:1px solid var(--navy);padding-top:3px}
.menu-btn{left:1036px;top:48px;width:58px;height:28px;border:1px solid #bbb;font-size:11px;color:#666;display:flex;align-items:center;justify-content:center;gap:4px}
.login-btn{left:1100px;top:46px;width:58px;height:32px;background:var(--navy);color:#fff;font-size:13px;display:flex;align-items:center;justify-content:center;border-radius:2px}
.hero{left:0;top:118px;width:1200px;height:482px;background:linear-gradient(180deg,#7fa0c4 0%,#a9bdd3 35%,#6f6a62 62%,#3c3631 100%)}
.hero-loco{left:450px;top:10px;width:360px;height:300px;background:radial-gradient(ellipse at center,#b8422a 0%,#8a3222 45%,rgba(70,40,30,0) 75%)}
.hero-title{left:0;top:448px;width:1200px;text-align:center;color:#fff;font-family:"Libre Baskerville",Georgia,serif;font-weight:700;font-size:42px;text-shadow:0 2px 6px rgba(0,0,0,.45)}
.hero-sub{left:0;top:498px;width:1200px;text-align:center;color:#fff;font-family:"Montserrat",Arial,sans-serif;font-weight:600;font-size:17px;line-height:1.4;text-transform:uppercase;letter-spacing:.5px;text-shadow:0 1px 4px rgba(0,0,0,.5)}
.hero-dots{left:578px;top:570px;display:flex;gap:6px}
.hero-dots i{width:9px;height:9px;border-radius:50%;background:rgba(255,255,255,.55);display:block}
.hero-dots i:first-child{background:#fff}
.arrow{top:340px;width:26px;height:70px;background:rgba(0,0,0,.35)}
.section-title{left:0;width:1200px;text-align:center;color:var(--navy);font-family:"Old Standard TT",Georgia,serif;font-size:22px;text-transform:uppercase;letter-spacing:.5px}
.feature{left:0;width:1200px}
.panel{background:var(--panel);color:#fff;padding:0 22px}
.panel h2{font-family:"Libre Baskerville",Georgia,serif;font-size:22px;line-height:1.35;font-weight:700;margin-bottom:8px}
.panel p{font-size:15px;line-height:1.3;margin-bottom:14px;text-align:justify}
.btn{display:inline-block;background:var(--navy);border:1px solid #fff;color:#fff;font-size:17px;padding:6px 16px}
.band{left:0;width:1200px;background:var(--navy)}
.field-label{color:#fff;font-size:16px}
.field-label small{font-size:10px;margin-left:6px}
.field{width:267px;height:32px;background:#fff;border-radius:2px}
.send{width:118px;height:33px;background:linear-gradient(90deg,#9b9b9b,#dcdcdc 55%,#7a7a7a);color:var(--navy-deep);font-size:16px;display:flex;align-items:center;justify-content:center}
.feed{left:836px;top:2973px;width:258px;height:265px;background:#fff;border-radius:4px;font-family:"Montserrat",Arial,sans-serif;font-size:10px;color:#333}
.contact-item{top:3384px;width:300px;text-align:center;color:#fff;font-family:"EB Garamond",Georgia,serif;font-size:18px}
.contact-item svg{display:block;margin:0 auto 10px}
.copyright{left:0;top:3522px;width:1200px;height:28px;background:#000;color:#ddd;font-size:11px;font-family:"Montserrat",Arial,sans-serif;text-align:center;line-height:28px}
</style>
</head>
<body>

<div class="abs topbar"></div>

<header class="abs header">
  <div class="abs brand">
    <div class="brand-mark">LFC</div>
    <div class="brand-name">Lakeshore Freightways Council</div>
  </div>
  <div class="abs menu-btn">Menu
    <svg width="10" height="8" viewBox="0 0 10 8"><path d="M0 1h10M0 4h10M0 7h10" stroke="#666" stroke-width="1.2"/></svg>
  </div>
  <div class="abs login-btn">Login</div>
</header>

<section class="abs hero" role="img" aria-label="Photo of a freight locomotive approaching a railroad crossing signal in winter light">
  <div class="abs hero-loco"></div>
</section>
<div class="abs arrow" style="left:0;top:340px"></div>
<div class="abs arrow" style="left:1174px;top:320px"></div>
<div class="abs hero-title">Railroad company investments</div>
<div class="abs hero-sub">Along with education, safety-enhancing technologies &amp; training<br>have helped ensure that train accidents are at an all-time low.</div>
<div class="abs hero-dots"><i></i><i></i><i></i><i></i><i></i></div>

<h2 class="abs section-title" style="top:618px">What We Do</h2>
<section class="abs feature" style="top:670px;height:473px;background:linear-gradient(90deg,#8a6a45 0%,#a8927a 30%,#6e6a66 55%,#4c3f35 100%)" role="img" aria-label="Photo of railroad tracks stretching into the distance through dry grass"></section>
<div class="abs panel" style="left:658px;top:670px;width:431px;height:473px;padding-top:100px">
  <h2>The LFC reviews all introduced legislation in the House &amp; Senate.</h2>
  <p style="font-size:14px">Proposed legislation affecting the rail industry is shared with our members. Final industry positions regarding legislation are then communicated to the legislature. We pursue the same activity with appropriate personnel in the state departments and the legislative rules process.</p>
  <span class="btn">Learn More</span>
</div>

<h2 class="abs section-title" style="top:1160px">Who We Are</h2>
<section class="abs feature" style="top:1212px;height:480px;background:linear-gradient(90deg,#2f4a22 0%,#3e5a2c 30%,#8a8a86 60%,#b3b0a0 80%,#6d8a3e 100%)" role="img" aria-label="Photo of a yellow freight train passing green trees"></section>
<div class="abs panel" style="left:166px;top:1212px;width:431px;height:480px;padding-top:150px">
  <p>The Lakeshore Freightways Council (LFC) is a non-profit trade association that represents the interests of freight railroads operating in the Lakeshore region. LFC members range in size from large Class I interstate carriers to smaller regional carriers and shortline railroads. LFC members account for over 95% of all freight rail moved in the region.</p>
  <span class="btn">Learn More</span>
</div>

<h2 class="abs section-title" style="top:1716px">How to Join LFC</h2>
<section class="abs feature" style="top:1775px;height:481px;background:linear-gradient(120deg,#2a2a2a 0%,#8a8a8a 35%,#4a4a4a 60%,#bdbdbd 100%)" role="img" aria-label="Black and white photo of curving railroad tracks and a switch"></section>
<div class="abs panel" style="left:748px;top:1775px;width:431px;height:481px;padding-top:92px">
  <p>LFC membership is open to any freight railroad with regional operations. Please contact the LFC office for membership information.</p>
  <p>Companies which supply goods or services to the railroad industry are eligible for a non-voting Associate Membership. Annual dues are $1,000 per year for supplier members.</p>
  <p>Please click HERE to download the LFC Associate Membership application. Return a completed form to info@lakeshorefreightwayscouncil.com or mail to our mailing address.</p>
  <span class="btn">Meet our Members</span>
</div>

<h2 class="abs section-title" style="top:2291px">Resources</h2>
<section class="abs feature" style="top:2353px;height:518px;background:linear-gradient(90deg,#6a5a50 0%,#9a8f88 35%,#e0742a 55%,#e88a2e 70%,#d8c838 85%,#b5a9a2 100%)" role="img" aria-label="Photo of an orange and yellow locomotive in the snow"></section>
<div class="abs panel" style="left:154px;top:2353px;width:428px;height:518px;padding-top:205px">
  <p>The Lakeshore Freightways Council (LFC) is a non-profit trade association that represents the interests of freight railroads operating in the Lakeshore region. LFC members range in size from large Class I interstate carriers to smaller regional carriers and shortline railroads. LFC members account for over 95% of all freight rail moved in the region.</p>
</div>

<h2 class="abs section-title" style="top:2902px;left:0;width:592px">Join our Newletter List</h2>
<h2 class="abs section-title" style="top:2902px;left:832px;width:270px">Follow LFC</h2>

<section class="abs band" style="top:2954px;height:320px"></section>
<div class="abs field-label" style="left:107px;top:2990px">Your Name<small>( required )</small></div>
<div class="abs field" style="left:107px;top:3022px"></div>
<div class="abs field-label" style="left:107px;top:3081px">Your Email<small>( required )</small></div>
<div class="abs field" style="left:107px;top:3113px"></div>
<div class="abs send" style="left:107px;top:3180px">Send</div>

<aside class="abs feed">
  <div style="padding:8px 10px;border-bottom:1px solid #e3e3e3;font-size:12px"><b>Tweets</b> <span style="color:#3a7fc4;font-size:10px">by @LakeFreightLine</span></div>
  <div style="padding:6px 10px 0 10px;color:#888;font-size:9px">LFC Retweeted</div>
  <div style="display:flex;gap:8px;padding:4px 10px">
    <div style="width:28px;height:28px;background:#b9b9b9;flex:none"></div>
    <div><b>Governor Dana Whitlow</b> <span style="color:#888">@dwhitlow</span><br>Today is a day to pause and remember those who were lost here years ago. #Remember</div>
  </div>
  <div role="img" aria-label="Photo of a memorial gathering under a flag" style="margin:6px 10px 0 46px;height:110px;background:linear-gradient(180deg,#7f8fa3,#5a6472 60%,#a05058)"></div>
  <div style="position:absolute;bottom:8px;left:10px;right:10px;display:flex;justify-content:space-between;color:#3a7fc4;font-size:9px"><span>Embed</span><span>View timeline</span></div>
</aside>

<h2 class="abs section-title" style="top:3305px">Get in Touch with Us</h2>

<section class="abs band" style="top:3361px;height:161px;background:repeating-linear-gradient(90deg,var(--navy) 0 3px,#0f0d7a 3px 6px)"></section>
<div class="abs contact-item" style="left:-20px">
  <svg width="34" height="34" viewBox="0 0 24 24"><path fill="#fff" d="M6.6 10.8a15 15 0 0 0 6.6 6.6l2.2-2.2c.3-.3.7-.4 1-.2 1.1.4 2.3.6 3.6.6.6 0 1 .4 1 1V20c0 .6-.4 1-1 1A17 17 0 0 1 3 4c0-.6.4-1 1-1h3.5c.6 0 1 .4 1 1 0 1.3.2 2.5.6 3.6.1.3 0 .7-.2 1z"/></svg>
  (555) 304-7180
</div>
<div class="abs contact-item" style="left:153px">
  <svg width="44" height="34" viewBox="0 0 26 20"><rect x="6" y="0" width="14" height="6" fill="#fff"/><rect x="0" y="7" width="26" height="9" rx="1" fill="#fff"/><rect x="6" y="13" width="14" height="7" fill="#fff" stroke="#0c0a70" stroke-width="1"/></svg>
  (555) 304-7181
</div>
<div class="abs contact-item" style="left:380px;width:400px">
  <svg width="54" height="34" viewBox="0 0 32 20"><rect x="0" y="0" width="32" height="20" fill="#fff"/><path d="M0 0l16 11L32 0M0 20l12-10M32 20L20 10" stroke="#0c0a70" stroke-width="1.5" fill="none"/></svg>
  info@lakeshorefreightwayscouncil.com
</div>
<div class="abs contact-item" style="left:809px">
  <svg width="26" height="36" viewBox="0 0 18 26"><path fill="#fff" d="M9 0a9 9 0 0 0-9 9c0 7 9 17 9 17s9-10 9-17a9 9 0 0 0-9-9zm0 13a4 4 0 1 1 0-8 4 4 0 0 1 0 8z"/></svg>
  48 Harbor Street, Suite 210 Port Alden<br>40512
</div>

<footer class="abs copyright">Copyright © 2017 Lakeshore Freightways Council</footer>

</body>
</html>
```